Fernbrook Pet Showcase Ticket Card Design

We’re looking to create a complimentary “ticket” card for Fernbrook Pet Showcase that can be handed out physically. We host an event for cat lovers. The card should feel special and collectible. Size will be a standard business card (3.5" x 2") Orientation is open to designer recommendation. This ticket will be used as a complimentary entry pass for select guests, partners, & giveaways. Key elements to Include are the Fernbrook Pet Showcase logo (provided), the words “Complimentary Ticket” or similar wording (open to creative phrasing and cat puns) A blank space for the Event date (to be written in) & Ticket number (to be written in) . Event Name is always "Fernbrook Pet Bazaar & Rehoming Day". We want the ticket to feel clean & modern but slightly playful with a cat-inspired touch (think clever, not kitschy). Could include a subtle cat motif or texture (e.g., whisker lines, paw detail, soft patterning) Open to unique layout ideas that still leave clear writing space. Avoid overcrowding of elements. Ticket should also have fine print "This ticket is not redeemable for cash and cannot be combined with any other offers or discounts, can only be used for the date indicated"

Target Market(s)

Women

Industry/Entity Type

pets

Colors
6B429C
8869AF
B7A5CE
E3DAEB
F3F0F8

Requirements
Must have
• Fernbrook Pet Showcase Logo & words around complimentary ticket as well as the fine print
Nice to have
• cat-inspired touch (think clever, not kitschy). Could include a subtle cat motif or texture (e.g., whisker lines, paw detail, soft patterning)
Should not have
• should not look cartoony

```html
<!DOCTYPE html>
<html lang="en">
<head>
<meta charset="utf-8">
<title>Fernbrook Pet Showcase – Complimentary Entry Pass</title>
<link rel="stylesheet" href="https://fonts.googleapis.com/css2?family=Cinzel:wght@500;600&family=Josefin+Sans:wght@600;700&family=Lato:wght@400;700&display=swap">
<style>
  :root {
    --purple-deep: #6B429C;
    --purple-mid: #8869AF;
    --purple-soft: #B7A5CE;
    --lilac: #E3DAEB;
    --mist: #F3F0F8;
    --card: #ECEAEF;
    --ink: #1c1a1f;
    --stage: #dcdcdc;
  }
  * { box-sizing: border-box; margin: 0; padding: 0; }
  html, body { width: 1200px; height: 783px; overflow: hidden; background: var(--stage); }
  .canvas { position: relative; width: 1200px; height: 783px; }

  .ticket {
    position: absolute; left: 400px; top: 41px;
    width: 400px; height: 700px;
    background: var(--card);
    box-shadow: 0 6px 24px rgba(0,0,0,.12);
  }

  .brand {
    position: absolute; top: 46px; left: 0; right: 0;
    display: flex; align-items: center; justify-content: center; gap: 12px;
  }
  .brand-dot { width: 18px; height: 18px; border-radius: 50%; background: var(--ink); }
  .brand-name {
    font-family: "Josefin Sans", sans-serif; font-weight: 700;
    font-size: 30px; line-height: 1.05; color: var(--ink);
    text-transform: uppercase; letter-spacing: 1px; text-align: center;
  }

  .event-name {
    position: absolute; top: 160px; left: 0; right: 0;
    display: flex; align-items: center; justify-content: center; gap: 14px;
  }
  .event-name .rule { flex: 1; height: 2px; background: var(--purple-mid); max-width: 46px; }
  .event-name p {
    font-family: "Josefin Sans", sans-serif; font-weight: 600;
    font-size: 19px; line-height: 1.15; color: var(--purple-mid);
    text-transform: uppercase; text-align: center; letter-spacing: .5px;
  }

  .pass-frame {
    position: absolute; left: 40px; top: 238px; width: 336px; height: 392px;
    border: 3px solid var(--purple-soft); border-radius: 28px;
  }

  .pass-title {
    position: absolute; top: 268px; left: 40px; width: 336px; text-align: center;
    font-family: "Cinzel", serif; color: var(--ink);
  }
  .pass-title .eyebrow { font-size: 25px; font-weight: 600; letter-spacing: 1px; }
  .pass-title .headline { font-size: 50px; font-weight: 500; line-height: 1; margin-top: 4px; }

  .tagline {
    position: absolute; top: 400px; left: 40px; width: 336px; text-align: center;
    font-family: "Josefin Sans", sans-serif; font-weight: 600;
    font-size: 21px; line-height: 1.2; color: var(--purple-deep);
  }

  .cat-motif {
    position: absolute; left: 10px; top: 455px; width: 92px; height: 200px;
    border-radius: 40px 40px 20px 30px;
    background: linear-gradient(180deg, rgba(183,165,206,.35), rgba(227,218,235,.2));
  }

  .field {
    position: absolute; left: 110px; width: 250px; height: 56px;
    background: var(--mist); border: 3px solid var(--purple-soft);
    border-radius: 28px; padding: 18px 0 0 20px;
    font-family: "Josefin Sans", sans-serif; font-weight: 700;
    font-size: 15px; color: var(--purple-deep); text-transform: uppercase;
  }
  .field.date { top: 482px; }
  .field.number { top: 550px; }

  .fine-print {
    position: absolute; left: 30px; right: 30px; top: 645px;
    font-family: "Lato", sans-serif; font-size: 12.5px; line-height: 1.3;
    color: var(--purple-deep); text-align: center;
  }
</style>
</head>
<body>
<main class="canvas">
  <article class="ticket">
    <header class="brand">
      <span class="brand-dot"></span>
      <h1 class="brand-name">Fernbrook<br>Pet Showcase</h1>
    </header>

    <div class="event-name">
      <span class="rule"></span>
      <p>Fernbrook Pet Bazaar<br>&amp; Rehoming Day</p>
      <span class="rule"></span>
    </div>

    <div class="pass-frame"></div>

    <h2 class="pass-title">
      <span class="eyebrow">Complimentary</span><br>
      <span class="headline">Entry Pass</span>
    </h2>

    <p class="tagline">A Paws-itively Free Day<br>of Feline Fun</p>

    <div class="cat-motif" role="img" aria-label="Line drawing of a seated cat seen from behind, with curled tail"></div>

    <div class="field date">Event Date</div>
    <div class="field number">Ticket No</div>

    <p class="fine-print">This ticket is not redeemable for cash and cannot be combined with any other offers or discounts, can only be used for the date indicated.</p>
  </article>
</main>
</body>
</html>
```